Dietitian clinic needs a business card design

We need a business card design for a new dietitian group based in Singapore called "Lantern and Tide". We provide expert, personalised nutrition care to support a wide range of health needs, from chronic conditions to mindful eating. Our team also offers consulting, speaking, and tailored solutions for healthcare providers, organisations, and food services.

Target Market(s)

Adults

Industry/Entity Type

Healthcare

Contact Information for Business Card

Name, position, contact number, email, website address, our logo

Requirements
Nice to have
• Clean, professional but welcoming look

```html
<!DOCTYPE html>
<html lang="en">
<head>
<meta charset="utf-8">
<title>Lantern and Tide – Business Card</title>
<link href="https://fonts.googleapis.com/css2?family=Playfair+Display:wght@700;800&family=Roboto:wght@400&display=swap" rel="stylesheet">
<style>
  :root {
    --navy: #143f52;
    --navy-deep: #0f3446;
    --paper: #f3f3f1;
    --ink-grey: #5a5d60;
    --stage: #e2e2e2;
    --white: #ffffff;
  }
  * { box-sizing: border-box; margin: 0; padding: 0; }
  html, body {
    width: 1200px; height: 900px; overflow: hidden;
    background: var(--stage);
  }
  .sheet {
    width: 1200px; height: 900px;
    display: flex; align-items: center; justify-content: center; gap: 40px;
  }
  .card {
    width: 540px; height: 309px; position: relative;
    box-shadow: 0 6px 18px rgba(0,0,0,0.12);
  }

  /* Back of card */
  .card-back {
    background: var(--navy);
  }
  .card-back .pattern-area {
    position: absolute; inset: 0;
    background: linear-gradient(135deg, #174a60 0%, var(--navy-deep) 100%);
  }
  .card-back .brand {
    position: absolute; left: 50%; top: 50%; transform: translate(-50%, -50%);
    display: flex; align-items: center; gap: 10px;
    font-family: "Playfair Display", serif; font-weight: 700;
    font-size: 22px; color: var(--white); white-space: nowrap;
  }
  .card-back .brand .dot {
    width: 14px; height: 14px; border-radius: 50%; background: var(--white);
  }

  /* Front of card */
  .card-front {
    background: var(--paper);
    font-family: "Roboto", sans-serif;
  }
  .rule-top {
    position: absolute; left: 58px; top: 72px; width: 420px;
    border-top: 1.2px solid var(--navy);
  }
  .identity { position: absolute; left: 40px; top: 84px; }
  .identity .name {
    font-family: "Playfair Display", serif; font-weight: 800;
    font-size: 30px; color: var(--navy); line-height: 1.05; letter-spacing: 0.3px;
  }
  .identity .role {
    font-size: 17px; color: var(--ink-grey); margin-top: 3px;
  }
  .rule-mid {
    position: absolute; left: 40px; top: 152px; width: 250px;
    border-top: 1.2px solid var(--navy);
  }
  .contacts {
    position: absolute; left: 40px; top: 174px; list-style: none;
    font-size: 12.5px; color: var(--ink-grey); line-height: 1.3;
  }
  .contacts li { display: flex; align-items: flex-start; gap: 7px; margin-bottom: 3px; }
  .contacts li.address { margin-bottom: 9px; }
  .contacts svg { width: 12px; height: 12px; flex: none; margin-top: 2px; fill: var(--navy); }
  .contacts svg.stroke { fill: none; stroke: var(--navy); stroke-width: 1.6; }
  .brand-front {
    position: absolute; right: 34px; top: 110px;
    display: flex; align-items: center; gap: 9px;
    font-family: "Playfair Display", serif; font-weight: 700;
    font-size: 23px; color: var(--navy); white-space: nowrap;
  }
  .brand-front .dot {
    width: 14px; height: 14px; border-radius: 50%; background: var(--navy);
  }
</style>
</head>
<body>
<main class="sheet">

  <section class="card card-back" aria-label="Business card, back">
    <div class="pattern-area" role="img" aria-label="Embossed repeating brand pattern on deep navy"></div>
    <div class="brand"><span class="dot"></span>Lantern and Tide</div>
  </section>

  <section class="card card-front" aria-label="Business card, front">
    <div class="rule-top"></div>
    <div class="identity">
      <h1 class="name">Dara Linwood</h1>
      <p class="role">Founder &amp; CEO</p>
    </div>
    <div class="rule-mid"></div>

    <ul class="contacts">
      <li class="address">
        <svg viewBox="0 0 24 24" aria-hidden="true"><path d="M12 1a8 8 0 0 0-8 8c0 6 8 14 8 14s8-8 8-14a8 8 0 0 0-8-8zm0 11a3 3 0 1 1 0-6 3 3 0 0 1 0 6z"/></svg>
        <span>14 Harbour Lane,<br>Northfield, ON K2P 4R7</span>
      </li>
      <li>
        <svg viewBox="0 0 24 24" aria-hidden="true"><path d="M6.6 10.8a15 15 0 0 0 6.6 6.6l2.2-2.2a1 1 0 0 1 1-.25 11.4 11.4 0 0 0 3.6.57 1 1 0 0 1 1 1V20a1 1 0 0 1-1 1A17 17 0 0 1 3 4a1 1 0 0 1 1-1h3.5a1 1 0 0 1 1 1c0 1.25.2 2.45.57 3.57a1 1 0 0 1-.25 1z"/></svg>
        <span>(555) 010-4821</span>
      </li>
      <li>
        <svg class="stroke" viewBox="0 0 24 24" aria-hidden="true"><rect x="2" y="5" width="20" height="14" rx="1"/><path d="M2 6l10 7 10-7"/></svg>
        <span>info@lanternandtide.com</span>
      </li>
      <li>
        <svg class="stroke" viewBox="0 0 24 24" aria-hidden="true"><circle cx="12" cy="12" r="10"/><path d="M2 12h20M12 2c3 3 3 17 0 20M12 2c-3 3-3 17 0 20"/></svg>
        <span>www.lanternandtide.com</span>
      </li>
    </ul>

    <div class="brand-front"><span class="dot"></span>Lantern and Tide</div>
  </section>

</main>
</body>
</html>
```